Charity donation cards

I need a card in an envelope that would be given out to people and they would put their donations along with their details (name and email) and give it back to us (dropped in acrylic boxes at events etc).

The card should be a medium size, bi or tri fold to be able to fit all the information i require.

The Sarwa Fund

The Bright Meadow Centre is dedicated to providing the much needed support to families and children struggling with their differences through a holistic and comprehensive approach that includes detailed evaluations, therapy programs and support services to help unlock the potential in every child.

We are so proud to be able to help empower our society by dedicating our business to the mental, physical and social well being of our younger community and pledging all our net profits to help ensure no child is ever left behind.

Professional services can often be expensive. Our Sarwa Fund helps support families requiring financial aid. We believe every child deserves the opportunity to succeed and no child should be left behind.

How can you help?

Gift the therapies to the children that need it the most. We welcome new sponsors, appreciate your gifts and gratefully accept your contributions as we expand to increase the number of children we can serve.

Name:
Email:
Amount:

We accept cash, checks or credit card payments at The Bright Meadow Centre.

Gift cards should be dropped in the designated acrylic boxes at TBMC or the event.

Please email sarwafund@kovelmint.ae for more information on the process.
Http://www.kovelmint.ae

Target Market(s)

These cards will be placed in the reception for our clients to donate.

We will also be working with party planners. Some parents don't want people to get them gifts for their kids birthday party so they want to use this instead.

Industry/Entity Type

Charity

Requirements
Must have
• The same feel as our centre Http://www.kovelmint.ae
• our website, email and contact number
Nice to have
• Go to our website and feel free to take ideas and content.
• The design should be clean and simple.
• High light the key words in the text with bold and maybe in green to make it pop out.
Should not have
• Do not use the word donate in any print material. The word should be gift.

```html
<!DOCTYPE html>
<html lang="en">
<head>
<meta charset="utf-8">
<title>Gift for a Smile – Fold Card</title>
<link href="https://fonts.googleapis.com/css2?family=PT+Sans:ital,wght@0,400;0,700;1,400&family=Chewy&display=swap" rel="stylesheet">
<style>
  :root{
    --paper:#ffffff;
    --grey-dark:#a9abae;
    --grey-mid:#c9cacc;
    --grey-light:#ececed;
    --rule:#8c8d90;
    --ink:#3a3a3c;
    --ink-soft:#555658;
    --green:#7cc242;
    --green-shadow:#3f6e1a;
    --crop:#9a9a9a;
    --logo-ink:#6d6e71;
    --logo-dot:#2bb3c9;
  }
  *{box-sizing:border-box;margin:0;padding:0}
  html,body{width:1200px;height:1000px;overflow:hidden;background:var(--paper)}
  body{position:relative;font-family:"PT Sans",Tahoma,sans-serif;color:var(--ink)}

  .crop-marks{position:absolute;inset:0;width:1200px;height:1000px}
  .crop-marks line{stroke:var(--crop);stroke-width:1}
  .crop-marks .fold{stroke-dasharray:4 3}

  .panel{position:absolute;overflow:hidden}
  .panel-outer{left:108px;top:195px;width:440px;height:613px}
  .panel-inner{left:618px;top:190px;width:437px;height:618px}

  .outer-back{position:absolute;left:0;top:0;width:100%;height:305px;
    background:radial-gradient(ellipse 170px 130px at 215px 60px,#fff 0%,#f2f2f3 30%,var(--grey-mid) 75%,var(--grey-dark) 100%);}
  .outer-front{position:absolute;left:0;top:305px;width:100%;height:308px;
    background:radial-gradient(ellipse 260px 200px at 230px 150px,#fbfbfb 0%,#e6e6e7 55%,var(--grey-mid) 100%);}
  .trim-frame{position:absolute;border:1px solid var(--rule);pointer-events:none}
  .panel-outer .trim-frame{left:10px;top:8px;width:420px;height:595px}
  .panel-inner .trim-frame{left:10px;top:13px;width:419px;height:595px}

  .brand{display:flex;align-items:center;gap:8px;font-family:"PT Sans",Tahoma,sans-serif;color:var(--logo-ink);font-weight:400;line-height:1.05}
  .brand-dot{flex:none;border-radius:50%;border:2px solid var(--logo-dot)}
  .brand-back{position:absolute;left:140px;top:30px;transform:rotate(180deg);font-size:17px;width:150px}
  .brand-back .brand-dot{width:42px;height:42px}

  .gift-title{position:absolute;left:28px;top:335px;font-family:"Chewy",cursive;color:var(--green);
    font-size:30px;line-height:.82;text-shadow:1px 2px 2px var(--green-shadow)}
  .gift-title .small{font-size:15px;display:block;padding-left:28px}

  .decor{position:absolute;left:0;top:0;width:440px;height:613px}
  .tagline{position:absolute;left:32px;top:576px;font-style:italic;font-size:12.5px;color:var(--ink-soft)}

  .brand-tab{position:absolute;background:#fff;border-radius:9px;box-shadow:1px 3px 5px rgba(0,0,0,.35)}
  .panel-outer .brand-tab{left:295px;top:542px;width:160px;height:43px;padding:6px 10px}
  .panel-outer .brand-tab .brand{font-size:11px}
  .panel-outer .brand-tab .brand-dot{width:24px;height:24px}
  .corner-fold{position:absolute;right:0;bottom:0;width:14px;height:14px;
    background:linear-gradient(135deg,transparent 50%,var(--grey-dark) 50%)}

  .photo{position:absolute;left:0;top:0;width:437px;height:238px;
    background:radial-gradient(ellipse 120px 130px at 165px 110px,#b79a88 0%,#8d8279 45%,#b1aca6 80%,#c6c2bd 100%)}
  .inner-body{position:absolute;left:0;top:238px;width:437px;height:380px;
    background:linear-gradient(180deg,#d9d9da 0%,#c2c3c5 60%,#b2b3b6 100%)}
  .panel-inner .brand-tab{left:230px;top:165px;width:220px;height:85px;padding:12px 18px}
  .panel-inner .brand-tab .brand{font-size:17px}
  .panel-inner .brand-tab .brand-dot{width:58px;height:58px}

  .help-title{position:absolute;left:24px;top:320px;font-size:19.5px;font-weight:700;color:var(--ink)}
  .help-copy{position:absolute;left:51px;top:355px;width:339px;font-size:11.6px;line-height:1.3;color:var(--ink)}
  .help-copy p{text-align:justify;margin-bottom:12px}
  .help-copy p.plain{text-align:left}
  .fields{margin:-2px 0 14px;list-style:none}
  .fields li{display:flex;align-items:flex-end;height:19px}
  .fields .line{flex:1;border-bottom:1px dashed var(--rule);margin-left:4px;margin-bottom:3px}
  .help-copy b{font-weight:700}
</style>
</head>
<body>

<svg class="crop-marks" viewBox="0 0 1200 1000" aria-hidden="true">
  <line x1="118" y1="150" x2="118" y2="185"/><line x1="538" y1="150" x2="538" y2="185"/>
  <line x1="628" y1="150" x2="628" y2="185"/><line x1="1048" y1="150" x2="1048" y2="185"/>
  <line x1="118" y1="815" x2="118" y2="852"/><line x1="538" y1="815" x2="538" y2="852"/>
  <line x1="628" y1="815" x2="628" y2="852"/><line x1="1048" y1="815" x2="1048" y2="852"/>
  <line x1="62" y1="203" x2="97" y2="203"/><line x1="557" y1="203" x2="597" y2="203"/><line x1="1067" y1="203" x2="1102" y2="203"/>
  <line x1="62" y1="798" x2="97" y2="798"/><line x1="557" y1="798" x2="597" y2="798"/><line x1="1067" y1="798" x2="1102" y2="798"/>
  <line class="fold" x1="72" y1="500" x2="108" y2="500"/>
  <line class="fold" x1="548" y1="500" x2="618" y2="500"/>
  <line class="fold" x1="1055" y1="500" x2="1102" y2="500"/>
</svg>

<section class="panel panel-outer" aria-label="Card outside">
  <div class="outer-back">
    <div class="brand brand-back"><span class="brand-dot"></span><span>The Bright Meadow Centre</span></div>
  </div>
  <div class="outer-front"></div>

  <svg class="decor" viewBox="0 0 440 613">
    <defs>
      <linearGradient id="tile" x1="0" y1="0" x2="1" y2="1">
        <stop offset="0" stop-color="#ffffff"/><stop offset="1" stop-color="#b9babc"/>
      </linearGradient>
      <radialGradient id="blank-frame" cx=".5" cy=".5" r=".6">
        <stop offset="0" stop-color="#ffffff"/><stop offset="1" stop-color="#a9aaad"/>
      </radialGradient>
      <linearGradient id="portrait" x1="0" y1="0" x2="1" y2="1">
        <stop offset="0" stop-color="#6f4a35"/><stop offset=".5" stop-color="#c9957a"/><stop offset="1" stop-color="#3c4a3c"/>
      </linearGradient>
      <filter id="lift" x="-20%" y="-20%" width="140%" height="140%">
        <feDropShadow dx="1" dy="2" stdDeviation="2" flood-opacity=".35"/>
      </filter>
    </defs>
    <g class="tiles" filter="url(#lift)" stroke="#ffffff" stroke-width="1.5">
      <rect x="142" y="330" width="22" height="22" rx="3" fill="url(#tile)"/>
      <rect x="207" y="347" width="12" height="12" rx="2" fill="url(#tile)"/>
      <rect x="190" y="376" width="10" height="10" rx="2" fill="url(#tile)"/>
      <rect x="214" y="372" width="26" height="26" rx="3" fill="url(#tile)"/>
      <rect x="151" y="393" width="26" height="26" rx="3" fill="url(#tile)"/>
      <rect x="204" y="416" width="18" height="18" rx="2" fill="url(#tile)"/>
      <rect x="237" y="428" width="20" height="20" rx="2" fill="url(#tile)"/>
      <rect x="175" y="443" width="14" height="14" rx="2" fill="url(#tile)"/>
      <rect x="228" y="466" width="14" height="14" rx="2" fill="url(#tile)"/>
    </g>
    <g class="frame-blank" filter="url(#lift)">
      <polygon points="110,474 168,464 177,552 122,561" fill="#ffffff"/>
      <polygon points="118,482 161,474 169,545 128,552" fill="url(#blank-frame)"/>
    </g>
    <g class="frame-photo" filter="url(#lift)">
      <polygon points="278,356 378,350 370,525 278,497" fill="#ffffff"/>
      <polygon role="img" aria-label="Photo of a smiling child" points="288,366 366,361 360,510 288,488" fill="url(#portrait)"/>
    </g>
  </svg>

  <h2 class="gift-title">Gift<span class="small">for a</span>smile</h2>
  <p class="tagline">There are many more to fill with a smile,</p>

  <div class="brand-tab"><div class="brand"><span class="brand-dot"></span><span>The Bright Meadow Centre</span></div></div>
  <div class="trim-frame"></div>
  <div class="corner-fold"></div>
</section>

<section class="panel panel-inner" aria-label="Card inside">
  <div class="photo" role="img" aria-label="Photo of a child blowing colourful confetti from his hands"></div>
  <div class="inner-body"></div>
  <div class="brand-tab"><div class="brand"><span class="brand-dot"></span><span>The Bright Meadow Centre</span></div></div>
  <div class="trim-frame"></div>

  <h2 class="help-title">How can you help?</h2>
  <div class="help-copy">
    <p>Gift the therapies to the children that need it the most. We welcome new sponsors, appreciate your gifts and gratefully accept your contributions as we expand to increase the number of children we can serve.</p>
    <ul class="fields">
      <li>Name:<span class="line"></span></li>
      <li>Email:<span class="line"></span></li>
      <li>Amount:<span class="line"></span></li>
    </ul>
    <p class="plain">We accept cash, checks or credit card payments at The Bright Meadow Centre.</p>
    <p class="plain">Gift cards should be dropped in the designated acrylic boxes at TBMC or the event.</p>
    <p class="plain">Email - <b>sarwafund@kovelmint.ae</b><br>For more information on the process - <b>www.kovelmint.ae</b></p>
  </div>
</section>

</body>
</html>
```